Financial Advisor needs waiting room sign

I am a financial advisor that works with a number of accountants to develop prospects. I am looking for a 18"x24" sign to hang in their office waiting rooms to help develop prospect interest in my services. My original idea was to list all of our services in a jumbled way on the sign and on the bottom have something like "Confused? We have the answers?" "Questions - We have answers" Our logo on the bottom. While I think this is still a good idea when I try to design it - it does not work. I am open to other ideas. Here is a list of our services (list in no particular order) and I will attach our logo. List: Plovance, Plovance Supplement, Plovance Advantage, Truvely, Part A, Part B, Part D, Social Security, Turning 65, Annuities, Fixed Index Annuities, Rollovers, 401k, 403b, Investments, Stock Market, Mutual Funds, Term Insurance, Life Insurance, Final Expense, Long Term Care, Mortgage Protection, 403B / 457 Not for Profit Set Up, 403B / TSA Plans, Annuities, Asset Protection, Charitable Giving, College Funding, Estate Planning, Fixed Indexed Annuities, Guaranteed Income, IRA & 401(K) Assets and Planning, IRA, 401(K), 403(B) Rollovers, Lifetime Income Planning, Retirement Income Planning, Safe Money Options, Social Security, Tactical Asset Allocation

```html
<!DOCTYPE html>
<html lang="en">
<head>
<meta charset="utf-8">
<title>Harlow Ridge Capital – Waiting Room Sign</title>
<link href="https://fonts.googleapis.com/css2?family=Bree+Serif&display=swap" rel="stylesheet">
<style>
  :root {
    --frame-green: #4b7236;
    --fold-green: #3d5e2b;
    --band-green: #6ea844;
    --confused-green: #4a6f35;
    --panel: #ffffff;
    --mark-tint: #e3eedb;
    --ink-1: #3b5e22;
    --ink-2: #44692a;
    --ink-3: #4f7a30;
    --ink-4: #5a8a35;
    --ink-5: #66993b;
    --ink-6: #72a843;
    --ink-7: #7db44b;
    --logo-ink: #4a6f35;
  }
  * { margin: 0; padding: 0; box-sizing: border-box; }
  html, body { width: 901px; height: 1200px; overflow: hidden; background: var(--frame-green); }
  .sign {
    position: relative; width: 901px; height: 1200px;
    background: var(--frame-green);
    font-family: "Bree Serif", Georgia, serif;
  }
  .panel { position: absolute; left: 50px; top: 0; width: 801px; height: 1200px; background: var(--panel); }
  .mark {
    position: absolute; color: var(--mark-tint); line-height: 1;
    font-family: "Bree Serif", Georgia, serif;
  }
  .mark--a { left: 130px; top: 60px; font-size: 330px; }
  .mark--b { left: 420px; top: 340px; font-size: 180px; }
  .mark--c { left: 600px; top: 10px; font-size: 300px; }
  .mark--d { left: 160px; top: 560px; font-size: 260px; }
  .mark--e { left: 590px; top: 470px; font-size: 420px; }

  .service-line {
    position: absolute; left: 98px; width: 705px;
    white-space: nowrap; text-align: justify; text-align-last: justify;
    line-height: 1;
  }
  .s1  { top: 64px;  font-size: 43px; color: var(--ink-1); }
  .s2  { top: 122px; font-size: 32px; color: var(--ink-1); }
  .s3  { top: 168px; font-size: 44px; color: var(--ink-2); }
  .s4  { top: 229px; font-size: 27px; color: var(--ink-2); }
  .s5  { top: 274px; font-size: 20px; color: var(--ink-2); }
  .s6  { top: 310px; font-size: 41px; color: var(--ink-3); }
  .s7  { top: 358px; font-size: 49px; color: var(--ink-3); }
  .s8  { top: 423px; font-size: 29px; color: var(--ink-4); }
  .s9  { top: 472px; font-size: 32px; color: var(--ink-4); }
  .s10 { top: 519px; font-size: 40px; color: var(--ink-5); }
  .s11 { top: 574px; font-size: 40px; color: var(--ink-5); }
  .s12 { top: 629px; font-size: 35px; color: var(--ink-6); }
  .s13 { top: 681px; font-size: 32px; color: var(--ink-6); }
  .s14 { top: 730px; font-size: 31px; color: var(--ink-7); }
  .s15 { top: 776px; font-size: 40px; color: var(--ink-7); }

  .folds { position: absolute; left: 0; top: 0; }
  .answer-band {
    position: absolute; left: 22px; top: 885px; width: 858px; height: 158px;
    background: var(--band-green); text-align: center; line-height: 1;
  }
  .answer-band__question { display: block; margin-top: 28px; font-size: 52px; color: var(--confused-green); }
  .answer-band__reply { display: block; margin-top: 8px; font-size: 52px; color: #ffffff; letter-spacing: 0.5px; }

  .brand { position: absolute; left: 180px; top: 1086px; display: flex; align-items: center; gap: 22px; }
  .brand__dot { width: 70px; height: 70px; border-radius: 50%; background: var(--logo-ink); }
  .brand__text { color: var(--logo-ink); line-height: 1; }
  .brand__name { display: block; font-size: 38px; letter-spacing: 2px; }
  .brand__tagline { display: block; margin-top: 6px; font-size: 15px; letter-spacing: 4.5px; }
</style>
</head>
<body>
<main class="sign">
  <div class="panel"></div>
  <div aria-hidden="true">
    <span class="mark mark--a">?</span>
    <span class="mark mark--b">?</span>
    <span class="mark mark--c">?</span>
    <span class="mark mark--d">?</span>
    <span class="mark mark--e">?</span>
  </div>

  <p class="service-line s1">Plovance · Plovance Supplement</p>
  <p class="service-line s2">Truvely · Plovance Advantage · Rollovers</p>
  <p class="service-line s3">Social Security · Life Insurance</p>
  <p class="service-line s4">Part A, Part B, Part D403(B) Rollovers · Turning 65</p>
  <p class="service-line s5">403B / 457 Not for Profit Set Up · 403B / TSA Plans · 401k, 403b</p>
  <p class="service-line s6">Annuities · Fixed Index Annuities</p>
  <p class="service-line s7">Investments · Stock Market</p>
  <p class="service-line s8">Retirement Income Planning · Estate Planning</p>
  <p class="service-line s9">Lifetime Income Planning · Final Expense</p>
  <p class="service-line s10">Charitable Giving · Mutual Funds</p>
  <p class="service-line s11">Term Insurance · College Funding</p>
  <p class="service-line s12">Long Term Care · Mortgage Protection</p>
  <p class="service-line s13">Safe Money Options · Guaranteed Income</p>
  <p class="service-line s14">Tactical Asset Allocation · Asset Protection</p>
  <p class="service-line s15">IRA &amp; 401(K) Assets and Planning</p>

  <svg class="folds" width="901" height="900" aria-hidden="true">
    <polygon points="22,885 50,870 50,885" fill="var(--fold-green)"/>
    <polygon points="851,870 880,885 851,885" fill="var(--fold-green)"/>
  </svg>
  <section class="answer-band">
    <span class="answer-band__question">Confused?</span>
    <span class="answer-band__reply">We have the answers!</span>
  </section>

  <footer class="brand">
    <span class="brand__dot" aria-hidden="true"></span>
    <span class="brand__text">
      <span class="brand__name">HARLOW RIDGE CAPITAL</span>
      <span class="brand__tagline">INSURANCE AND FINANCIAL SERVICES</span>
    </span>
  </footer>
</main>
</body>
</html>
```